Keystone Physical Therapy needs a New website look and update!

New updated look. Most people do not know they can go directly to a physical therapist for care. Cost effective and specialized. Getting back to your life and activity is what we do. What we treat. Your first cost effective provider for pain" for example. We treat children to seniors. Theme should be warm, caring, individualized, respect your time, and cost -effective. Mobile phone ready. Encourage taking action to call and schedule to get back to life, sports, activity.
Add link to send appointment request or contact us now
Add link ( code) for patients to fill out intake form or appointment request. I want to add testimonials for other therapists.
***My current website is "brellowkeypt.net"

```html
<!DOCTYPE html>
<html lang="en">
<head>
<meta charset="utf-8">
<title>Keystone Physical Therapy</title>
<link href="https://fonts.googleapis.com/css2?family=Open+Sans:ital,wght@0,400;0,600;0,700;0,800;1,400&display=swap" rel="stylesheet">
<style>
:root{
  --blue:#3b7592;
  --blue-dark:#2f6580;
  --green:#9dcb2f;
  --green-dark:#86b21f;
  --text:#555;
  --light:#f4f4f4;
  --footer:#2b2b2b;
  --footer-text:#b9b9b9;
  --white:#fff;
}
*{box-sizing:border-box;margin:0;padding:0}
html,body{width:1200px;height:2586px;overflow:hidden}
body{font-family:"Open Sans",Arial,sans-serif;color:var(--text);background:var(--white);position:relative}
a{text-decoration:none;color:inherit}

/* header */
.site-header{position:relative;height:126px;border-top:4px solid var(--green);background:var(--white)}
.phone-tab{position:absolute;right:70px;top:-4px;width:250px;height:46px;background:var(--green);color:var(--white);
  border-radius:0 0 10px 24px;display:flex;align-items:center;justify-content:center;gap:10px;font-weight:700;font-size:21px}
.brand{position:absolute;left:78px;top:36px;display:flex;align-items:center;gap:12px}
.brand-mark{width:78px;height:78px;border-radius:50%;background:var(--blue)}
.brand-name{font-size:36px;font-weight:700;color:var(--blue);letter-spacing:-0.5px}
.main-nav{position:absolute;left:367px;top:84px;display:flex;gap:35px;font-size:13px;font-weight:600;color:#444;text-transform:uppercase}
.main-nav .active{color:var(--blue)}
.patients-btn{position:absolute;left:983px;top:72px;width:143px;height:44px;background:var(--blue);color:var(--white);
  font-weight:700;font-size:13px;display:flex;align-items:center;justify-content:center;text-transform:uppercase;border-radius:2px}

/* hero */
.hero{position:relative;height:534px;overflow:hidden}
.hero-photo{position:absolute;inset:0;background:radial-gradient(ellipse at 50% 60%,#3b5a72 0%,#1d3344 40%,#0a0f14 80%)}
.hero-content{position:relative;text-align:center;color:var(--white);padding-top:180px;text-shadow:0 2px 6px rgba(0,0,0,.5)}
.hero-content .kicker{font-size:40px;font-weight:800;line-height:46px}
.hero-content h1{font-size:56px;font-weight:800;line-height:62px}
.hero-content .place{font-size:40px;font-weight:800;line-height:46px}
.hero-btn{display:inline-flex;margin-top:22px;width:388px;height:53px;align-items:center;justify-content:center;background:var(--green);
  font-weight:700;font-size:22px;text-shadow:none}
.hero-arrow{position:absolute;top:247px;width:40px;height:40px;border:2px solid rgba(255,255,255,.8);border-radius:50%}
.hero-arrow.prev{left:59px}.hero-arrow.next{right:59px}
.hero-arrow svg{position:absolute;inset:0;margin:auto}

/* welcome */
.welcome{height:337px;text-align:center;padding-top:50px}
.section-title{font-size:27px;font-weight:700;color:var(--blue);text-transform:uppercase}
.welcome p{width:1010px;margin:14px auto 0;font-size:15px;line-height:26px;color:#555}
.welcome p+p{margin-top:2px}
.btn{display:inline-flex;align-items:center;justify-content:center;width:206px;height:51px;background:var(--green);color:var(--white);
  font-weight:700;font-size:14px;text-transform:uppercase}
.welcome .btn{margin-top:44px}

/* services */
.services{background:var(--light);height:706px;padding-top:48px;text-align:center;position:relative}
.service-grid{display:grid;grid-template-columns:512px 512px;gap:28px;width:1052px;margin:36px auto 0}
.service-card{height:229px;background:var(--white);position:relative;display:flex;align-items:flex-start;text-align:left;
  box-shadow:0 14px 14px -10px rgba(0,0,0,.18)}
.service-photo{position:absolute;left:10px;top:20px;width:186px;height:186px;border-radius:50%;border:12px solid #ececec;
  box-shadow:0 0 0 3px #f7f7f7}
.service-body{margin-left:215px;padding-top:50px;width:270px}
.service-body h3{font-size:14px;font-weight:700;color:var(--blue);text-transform:uppercase}
.service-body p{font-size:14px;line-height:24px;margin-top:6px;color:#555}
.service-body .more{display:block;margin-top:14px;font-size:13px;font-weight:700;color:var(--green);text-transform:uppercase}
.services .view-all{position:absolute;left:497px;top:679px;width:206px;height:51px}
.g1{background:linear-gradient(135deg,#f1d6c8,#3e64b7)}
.g2{background:linear-gradient(135deg,#3a2f2a,#c99a7a)}
.g3{background:linear-gradient(135deg,#9aa0a8,#4a4a52)}
.g4{background:linear-gradient(135deg,#2e6fa8,#d4b19a)}

/* testimonials & sidebar */
.lower{position:relative;height:564px}
.testimonials{position:absolute;left:76px;top:58px;width:690px}
.testimonials .section-title{text-align:left}
.testi-grid{display:grid;grid-template-columns:358px 328px;row-gap:26px;margin-top:26px}
.testi h4{font-size:14px;font-weight:700;color:var(--green);text-transform:uppercase}
.testi blockquote{font-style:italic;font-size:13px;line-height:24px;color:#555;margin-top:6px;width:326px}
.avatar{width:76px;height:76px;border-radius:50%;background:linear-gradient(#cfd6dc,#8c99a3);margin-top:14px;
  border:4px solid var(--blue);box-shadow:3px 0 0 0 var(--green)}
.store{position:absolute;left:793px;top:62px;width:333px;height:83px;background:linear-gradient(#4a4a4a,#2e2e2e);
  display:flex;align-items:center;gap:18px;padding-left:22px;color:var(--white)}
.store strong{display:block;font-size:25px;font-weight:800;line-height:28px}
.store span{color:var(--green);font-size:13px;font-weight:700;text-transform:uppercase}
.posts{position:absolute;left:793px;top:164px;width:333px;height:348px;border:1px solid #e3e3e3}
.posts-title{height:58px;background:#f1f1f1;font-size:27px;font-weight:700;color:var(--blue);padding:10px 18px;text-transform:uppercase}
.post{padding:18px 18px 0}
.post-head{display:flex;gap:14px}
.post-photo{width:107px;height:80px;flex:none;background:linear-gradient(#9fb5c8,#6d8c4e)}
.post-head h5{font-size:14px;font-weight:700;color:var(--green);line-height:19px;text-transform:uppercase}
.post p{font-size:13px;line-height:22px;margin-top:10px;color:#555}
.post time{display:block;font-size:11px;color:var(--green);margin-top:8px}
.posts-foot{position:absolute;left:0;right:0;bottom:0;height:46px;border-top:1px solid #e3e3e3;display:flex;align-items:center;
  gap:12px;padding-left:24px;font-size:12px;font-weight:700;color:#333;text-transform:uppercase}
.posts-foot i{width:11px;height:11px;background:var(--blue);display:block}

/* footer */
.site-footer{position:absolute;left:0;top:2293px;width:1200px;height:293px;background:var(--footer);border-top:5px solid var(--blue);color:var(--footer-text)}
.footer-brand{position:absolute;left:76px;top:78px;display:flex;align-items:center;gap:10px}
.footer-brand .brand-mark{width:66px;height:66px}
.footer-brand .brand-name{font-size:30px;color:var(--white)}
.copyright{position:absolute;left:76px;top:166px;font-size:11px;line-height:21px;color:#ddd}
.footer-col{position:absolute;top:50px}
.footer-col h6{font-size:12px;font-weight:700;color:var(--green);text-transform:uppercase;margin-bottom:6px}
.footer-col li{list-style:none;font-size:13px;line-height:26px;color:#ccc}
.col-map{left:378px}.col-services{left:560px}.col-news{left:884px}
.subscribe{display:flex;margin-top:8px}
.subscribe span{width:200px;height:38px;background:var(--white);color:#777;font-size:12px;padding:10px 10px}
.subscribe b{width:42px;height:38px;background:var(--blue);display:flex;align-items:center;justify-content:center}
.follow{margin-top:16px}
.social{display:flex;gap:17px;margin-top:10px}
.social i{width:18px;height:18px;border-radius:50%;background:#8d8d8d;display:block}
</style>
</head>
<body>

<header class="site-header">
  <a class="phone-tab" href="tel:3035550148">
    <svg width="18" height="18" viewBox="0 0 24 24"><path fill="#fff" d="M6.6 10.8a15 15 0 0 0 6.6 6.6l2.2-2.2a1 1 0 0 1 1-.25 11.4 11.4 0 0 0 3.6.57 1 1 0 0 1 1 1V20a1 1 0 0 1-1 1A17 17 0 0 1 3 4a1 1 0 0 1 1-1h3.5a1 1 0 0 1 1 1c0 1.25.2 2.45.57 3.57a1 1 0 0 1-.25 1z"/></svg>
    303-555-0148
  </a>
  <a class="brand" href="#"><span class="brand-mark"></span><span class="brand-name">Keystone</span></a>
  <nav class="main-nav">
    <a class="active" href="#">Home</a><a href="#">About Us</a><a href="#">Services</a><a href="#">FAQ</a>
    <a href="#">Forms</a><a href="#">Insurance</a><a href="#">Contact Us</a>
  </nav>
  <a class="patients-btn" href="#">Patients Care</a>
</header>

<section class="hero">
  <div class="hero-photo" role="img" aria-label="Swimmer in a blue cap doing butterfly stroke through splashing water"></div>
  <a class="hero-arrow prev" href="#"><svg width="14" height="14" viewBox="0 0 14 14"><path d="M9 2 4 7l5 5" stroke="#fff" stroke-width="2" fill="none"/></svg></a>
  <a class="hero-arrow next" href="#"><svg width="14" height="14" viewBox="0 0 14 14"><path d="m5 2 5 5-5 5" stroke="#fff" stroke-width="2" fill="none"/></svg></a>
  <div class="hero-content">
    <div class="kicker">Welcome To</div>
    <h1>Keystone Physical Therapy</h1>
    <div class="place">Based Brellow Springs, Colorado</div>
    <a class="hero-btn" href="#">SEND APPOINTMENT REQUEST</a>
  </div>
</section>

<section class="welcome">
  <h2 class="section-title">Welcome to our website</h2>
  <p>Welcome to Keystone Physical Therapy, southeast Denver's choice for healing and rehabilitation. Our therapist owned practice is committed to restoration, wellness and quality of life providing compassionate, skilled care to clients of all ages.</p>
  <p>Keystone Physical Therapy treats a wide range of injuries and conditions, whether you're recovering from surgery, returning to athletics or enhancing sports performance.</p>
  <a class="btn" href="#">Contact Us Now</a>
</section>

<section class="services">
  <h2 class="section-title">Therapy Services</h2>
  <div class="service-grid">
    <article class="service-card">
      <div class="service-photo g1" role="img" aria-label="Gloved hand performing dry needling on skin"></div>
      <div class="service-body"><h3>Dry Needling</h3>
        <p>Lorem ipsum dolor sit amet, consectetur adipisicing eitseo eiusmod tempor labore et dolore magna aliqua.</p>
        <a class="more" href="#">Learn More</a></div>
    </article>
    <article class="service-card">
      <div class="service-photo g2" role="img" aria-label="Therapist massaging a client's back"></div>
      <div class="service-body"><h3>Massage Therapy</h3>
        <p>Lorem ipsum dolor sit amet, consectetur adipisicing eitseo eiusmod tempor labore et dolore magna aliqua.</p>
        <a class="more" href="#">Learn More</a></div>
    </article>
    <article class="service-card">
      <div class="service-photo g3" role="img" aria-label="Pilates exercise session on a mat"></div>
      <div class="service-body"><h3>Pilates</h3>
        <p>Lorem ipsum dolor sit amet, consectetur adipisicing eitseo eiusmod tempor labore et dolore magna aliqua.</p>
        <a class="more" href="#">Learn More</a></div>
    </article>
    <article class="service-card">
      <div class="service-photo g4" role="img" aria-label="Therapist treating a patient's arm"></div>
      <div class="service-body"><h3>Laser and Infrared Therapy</h3>
        <p>Lorem ipsum dolor sit amet, consectetur adipisicing eitseo eiusmod tempor labore et dolore magna aliqua.</p>
        <a class="more" href="#">Learn More</a></div>
    </article>
  </div>
  <a class="btn view-all" href="#">View All Services</a>
</section>

<section class="lower">
  <div class="testimonials">
    <h2 class="section-title">Testimonials</h2>
    <div class="testi-grid">
      <div class="testi"><h4>Name Heading</h4><blockquote>" Lorem ipsum dolor sit amet, consectetur adipisicing eitseo eiusmod tempor labore et dolore magna aliqua enim ad minim veniam.."</blockquote><div class="avatar" role="img" aria-label="Client portrait"></div></div>
      <div class="testi"><h4>Name Heading</h4><blockquote>" Lorem ipsum dolor sit amet, consectetur adipisicing eitseo eiusmod tempor labore et dolore magna aliqua enim ad minim veniam.."</blockquote><div class="avatar" role="img" aria-label="Client portrait"></div></div>
      <div class="testi"><h4>Name Heading</h4><blockquote>" Lorem ipsum dolor sit amet, consectetur adipisicing eitseo eiusmod tempor labore et dolore magna aliqua enim ad minim veniam.."</blockquote><div class="avatar" role="img" aria-label="Client portrait"></div></div>
      <div class="testi"><h4>Name Heading</h4><blockquote>" Lorem ipsum dolor sit amet, consectetur adipisicing eitseo eiusmod tempor labore et dolore magna aliqua enim ad minim veniam.."</blockquote><div class="avatar" role="img" aria-label="Client portrait"></div></div>
    </div>
  </div>

  <a class="store" href="#">
    <svg width="44" height="38" viewBox="0 0 44 38"><path d="M2 4h7l5 20h22l5-14H12" fill="none" stroke="#9dcb2f" stroke-width="4" stroke-linejoin="round"/><path d="M12 10h29l-5 14H14z" fill="#9dcb2f"/><circle cx="16" cy="32" r="3.5" fill="#9dcb2f"/><circle cx="33" cy="32" r="3.5" fill="#9dcb2f"/></svg>
    <div><strong>ONLINE PT STORE</strong><span>Shop Now</span></div>
  </a>

  <aside class="posts">
    <div class="posts-title">Latest Posts</div>
    <div class="post">
      <div class="post-head">
        <div class="post-photo" role="img" aria-label="Coach and young pitcher on a baseball field"></div>
        <h5>Pitch count rules vary but mission is same: protect young arms</h5>
      </div>
      <p>Marcus Hale was playing for Ridgefield when he threw 280 pitches in a 15-inning, 2-1 district loss to Cedar Point, and its ace, Owen Pratt.</p>
      <time>21 hours ago</time>
    </div>
    <a class="posts-foot" href="#"><i></i>Find us online</a>
  </aside>
</section>

<footer class="site-footer">
  <div class="footer-brand"><span class="brand-mark"></span><span class="brand-name">Keystone</span></div>
  <p class="copyright">Copyright © 2017 Keystone Physical Therapy<br>All Right Reserved</p>
  <div class="footer-col col-map"><h6>Site Map</h6><ul><li>Home</li><li>About Us</li><li>Services</li><li>FAQ</li><li>Forms</li><li>Insurance</li><li>Contact Us</li></ul></div>
  <div class="footer-col col-services"><h6>Services</h6><ul><li>Manual Therapy/ Soft Tissue Mobilization</li><li>Laser and Infrared Therapy</li><li>Custom Orthotics and Foot Evaluations</li><li>Core Stabilization and Pilates</li><li>Alignment Training</li><li>Dry Needling</li></ul></div>
  <div class="footer-col col-news"><h6>Sign Up Newsletter</h6>
    <div class="subscribe"><span>Enter Email Address</span><b><svg width="12" height="16" viewBox="0 0 12 16"><path d="m3 2 6 6-6 6" stroke="#fff" stroke-width="2.5" fill="none"/></svg></b></div>
    <h6 class="follow">Follow Us</h6>
    <div class="social"><i></i><i></i><i></i><i></i><i></i><i></i><i></i></div>
  </div>
</footer>

</body>
</html>
```